Velmora Works Brochure Design Project

Our company requires a brochure for promoting our Corporate Training business.

Please use data from Corporate training brochure doc.

Dear Designers,

We have added new corporate brochure document into the project. Use this data to finish up your brochure.

Thanks,

Omar deswick

Reason: We have recently finalised the data that will go into the corporate brochure.

Reason: To get more better designs

Target Market(s)

Training Managers / Business Managers / Hiring Managers

Industry/Entity Type

Training

Requirements
Must have
• Corporate and Professional Look

```html
<!DOCTYPE html>
<html lang="en">
<head>
<meta charset="utf-8">
<title>Velmora Works – Corporate Training Brochure Cover</title>
<link href="https://fonts.googleapis.com/css2?family=Arimo:wght@400;500&display=swap" rel="stylesheet">
<style>
  :root {
    --paper: #ffffff;
    --panel-grey: #e1e1e1;
    --accent-blue: #a9c9dc;
    --brand-blue: #0f5aa6;
    --text-dark: #222222;
    --text-mid: #555555;
  }
  * { margin: 0; padding: 0; box-sizing: border-box; }
  html, body { width: 1200px; height: 849px; overflow: hidden; background: var(--paper); }
  .spread {
    position: relative;
    width: 1200px;
    height: 849px;
    font-family: "Arimo", Arial, sans-serif;
    color: var(--text-dark);
    overflow: hidden;
  }
  .spread__shapes { position: absolute; inset: 0; }
  .head-office {
    position: absolute;
    left: 119px;
    top: 616px;
  }
  .head-office__title { font-size: 12.5px; font-weight: 400; line-height: 16px; margin-bottom: 14px; }
  .head-office__address { font-size: 8.5px; line-height: 13.75px; font-style: normal; }
  .head-office__enquiry { font-size: 8px; line-height: 13px; margin-top: 15px; white-space: nowrap; }
  .headline {
    position: absolute;
    left: 750px;
    top: 661px;
    font-size: 17px;
    font-weight: 400;
    line-height: 20px;
    letter-spacing: 0.46em;
    color: var(--text-mid);
    white-space: nowrap;
  }
  .brand {
    position: absolute;
    right: 34px;
    top: 775px;
    display: flex;
    align-items: center;
    gap: 10px;
  }
  .brand__dot {
    width: 40px; height: 40px;
    border-radius: 50%;
    background: var(--brand-blue);
  }
  .brand__name {
    font-size: 22px;
    font-weight: 400;
    color: var(--brand-blue);
  }
</style>
</head>
<body>
<main class="spread">
  <svg class="spread__shapes" width="1200" height="849" viewBox="0 0 1200 849">
    <defs>
      <linearGradient id="greenery" x1="0" y1="0" x2="0.2" y2="1">
        <stop offset="0" stop-color="#9fc184"/>
        <stop offset="0.35" stop-color="#b8d3a2"/>
        <stop offset="0.6" stop-color="#eef2ea"/>
        <stop offset="0.85" stop-color="#f7f7f5"/>
        <stop offset="1" stop-color="#9a9c9e"/>
      </linearGradient>
      <linearGradient id="team" x1="0" y1="0.3" x2="1" y2="0.5">
        <stop offset="0" stop-color="#2c3036"/>
        <stop offset="0.08" stop-color="#3c4047"/>
        <stop offset="0.2" stop-color="#b98a72"/>
        <stop offset="0.33" stop-color="#d1a58c"/>
        <stop offset="0.45" stop-color="#3a302c"/>
        <stop offset="0.6" stop-color="#d8b39c"/>
        <stop offset="0.75" stop-color="#6b5143"/>
        <stop offset="0.88" stop-color="#d9c7cf"/>
        <stop offset="1" stop-color="#c8d9b8"/>
      </linearGradient>
      <linearGradient id="plaza" x1="0.3" y1="0" x2="0.6" y2="1">
        <stop offset="0" stop-color="#3f4a44"/>
        <stop offset="0.3" stop-color="#6f8a52"/>
        <stop offset="0.55" stop-color="#5a5550"/>
        <stop offset="0.75" stop-color="#9a6e48"/>
        <stop offset="1" stop-color="#b9b7b2"/>
      </linearGradient>
    </defs>

    <!-- left page -->
    <polygon class="photo-greenery" role="img" aria-label="Soft-focus photo of green foliage and daylight"
      points="0,0 70,0 185,125 52,849 0,849" fill="url(#greenery)"/>
    <polygon class="facet-blue" points="70,0 205,0 185,125" fill="var(--accent-blue)"/>
    <polygon class="facet-grey" points="205,0 600,0 600,580 185,125" fill="var(--panel-grey)"/>
    <polygon class="facet-grey-low" points="280,849 600,760 600,849" fill="var(--panel-grey)"/>
    <polygon class="facet-blue-low" points="458,770 600,705 600,830" fill="var(--accent-blue)"/>

    <!-- right page -->
    <polygon class="photo-team" role="img" aria-label="Photo of smiling business professionals in a training team, standing in an office corridor"
      points="600,0 1200,0 1200,435 680,665 600,580" fill="url(#team)"/>
    <polygon class="photo-plaza" role="img" aria-label="Photo of a modern office courtyard with planters and wooden benches"
      points="600,692 676,666 836,849 600,849" fill="url(#plaza)"/>
    <polygon class="facet-grey-foot" points="860,849 1200,812 1200,849" fill="var(--panel-grey)"/>
  </svg>

  <section class="head-office">
    <h2 class="head-office__title">Head Office</h2>
    <address class="head-office__address">
      Velmora Works Limited<br>
      Larkspur House, 1st Floor,<br>
      Halden Business Park,<br>
      Crestline Road, Westbay (W),<br>
      Northport – 400112. India.
    </address>
    <p class="head-office__enquiry">for any enquiries please email to hello@velmoraworks.com or fill form available at right hand side</p>
  </section>

  <h1 class="headline">ACTUAL HEADLINE</h1>

  <div class="brand">
    <span class="brand__dot"></span>
    <span class="brand__name">Velmora Works</span>
  </div>
</main>
</body>
</html>
```